Images Needed for Training Document

We are a staffing company that is working to help develop our leadership team. We have created a training document to help this team navigate quarterly review meetings, but need help with creating graphics/images to go with the text of the document. I am attaching the training document, with bold red notes where we need images/graphics.

If needed, I can also send a list of the exact type of images/graphics we are looking to add.

I am also attaching documents we use in other areas of the business, just to give an idea of what we typically have in our marketing.

```html
<!DOCTYPE html>
<html lang="en">
<head>
<meta charset="utf-8">
<title>Best Practices Verification – Options</title>
<link href="https://fonts.googleapis.com/css2?family=Poppins:wght@400;500;600;800&display=swap" rel="stylesheet">
<style>
  :root {
    --ink: #1a1a1a;
    --dark: #2a2a2a;
    --light: #efefef;
    --white: #ffffff;
    --blue: #0d62c0;
    --yellow: #efb80f;
    --red: #d93535;
    --orange: #ef7a3a;
  }
  * { box-sizing: border-box; margin: 0; padding: 0; }
  html, body { width: 1200px; height: 1200px; overflow: hidden; background: var(--white); }
  body { font-family: "Poppins", sans-serif; color: var(--ink); }
  .stage { position: absolute; left: 0; top: 0; width: 1920px; height: 1920px; transform: scale(0.625); transform-origin: 0 0; }

  .option-title { position: absolute; top: 508px; font-size: 46px; font-weight: 400; letter-spacing: 1px; transform: translateX(-50%); white-space: nowrap; }
  .option-title.one { left: 693px; }
  .option-title.two { left: 1240px; }

  .sheet { position: absolute; top: 626px; display: grid; }
  .sheet.one { left: 496px; width: 393px; grid-template-columns: 87px 306px; grid-template-rows: 47px 64px 64px 128px 81px 73px 79px 91px; }
  .sheet.two { left: 1044px; width: 393px; grid-template-columns: 87px 298px; column-gap: 8px; grid-template-rows: 47px 64px 64px 127px 81px 73px 78px 91px; row-gap: 8px; }

  .activity-head, .practice-head, .activity, .practices { display: flex; }
  .activity-head { align-items: center; justify-content: center; text-align: center; font-size: 8.5px; font-weight: 500; line-height: 9px; }
  .practice-head { align-items: center; justify-content: center; font-size: 13px; font-weight: 800; color: var(--white); }
  .activity { align-items: center; justify-content: center; text-align: center; font-size: 7.5px; font-weight: 600; color: var(--white); }
  .practices { padding: 8px 8px 0 19px; }

  .sheet.one .activity-head { background: var(--light); color: var(--ink); }
  .sheet.one .practice-head { background: var(--dark); border-radius: 2px 2px 0 0; }
  .sheet.one .practices.shade { background: var(--light); }
  .sheet.one .practices.plain { background: var(--white); }
  .activity.blue { background: var(--blue); }
  .activity.yellow { background: var(--yellow); }
  .activity.red { background: var(--red); }
  .practices.blue { --mark: var(--blue); }
  .practices.yellow { --mark: var(--yellow); }
  .practices.red { --mark: var(--red); }

  .sheet.two .activity-head { background: var(--dark); color: var(--white); border-radius: 3px; }
  .sheet.two .practice-head { background: var(--orange); border-radius: 3px; }
  .sheet.two .activity { background: var(--orange); border-radius: 3px; }
  .sheet.two .practices { background: var(--light); border-radius: 3px; --mark: var(--orange); }

  .checks { list-style: none; font-size: 6.6px; font-weight: 500; line-height: 8px; }
  .checks li { position: relative; margin-bottom: 4.7px; }
  .checks li::before { content: "→"; position: absolute; left: -10px; top: 0; color: var(--mark); font-weight: 600; }
</style>
</head>
<body>
<div class="stage">
  <h2 class="option-title one">Option-1</h2>
  <h2 class="option-title two">Option-2</h2>

  <section class="sheet one">
    <div class="activity-head">Recruiting<br>Activity</div>
    <div class="practice-head">Best Practices Verification</div>

    <div class="activity blue">CN Entered</div>
    <div class="practices shade blue"><ul class="checks">
      <li>Are they participating in your proactive recruiting schedule?</li>
      <li>What avenues do they use to source candidates? 1-10</li>
      <li>How well do they know how to parse?</li>
      <li>Are they matching every candidate that they call for an opportunity?</li>
    </ul></div>

    <div class="activity yellow">Contacts</div>
    <div class="practices plain yellow"><ul class="checks">
      <li>Confirm recruiter has Apex Recruit synced with MailDesk?</li>
      <li>Are they documenting each call they have with candidate?</li>
      <li>Confirm they are parsing ProLink messages into SubmitLog.</li>
      <li>Confirm they are following our screening process.</li>
    </ul></div>

    <div class="activity red">Matches</div>
    <div class="practices shade red"><ul class="checks">
      <li>Confirm they are able to ID the perfect candidate.</li>
      <li>Confirm they are going 1 through 10.</li>
      <li>Confirm they can efficiently go 1 through 10.</li>
      <li>Are they going narrow in their initial 1 through 10 search?</li>
      <li>Are they finishing 1 through 10 regardless if they find a candidate early in process?</li>
      <li>Identify what they determine in a candidate's credentials to match.</li>
      <li>Do they have a grasp on all open positions?</li>
      <li>Are there appropriate number of matches for each avenue?</li>
      <li>Have they posted the job? ProLink feed / NetBridge / Beacon Reach</li>
    </ul></div>

    <div class="activity blue">AIs</div>
    <div class="practices plain blue"><ul class="checks">
      <li>Do they proactively recruit on Mondays?</li>
      <li>Confirm they call, email, and ProLink connect with every match.</li>
      <li>Confirm that they continue to call and email every match they had the previous days before sourcing again.</li>
      <li>Confirm recruiter is "warming" voicemails through our past history with candidate or common ground with candidate.</li>
    </ul></div>

    <div class="activity yellow">Submittals</div>
    <div class="practices shade yellow"><ul class="checks">
      <li>Confirm matches are accurate toward job they are currently working.</li>
      <li>Are they working on the right requirement?</li>
      <li>Is the requirement's moderate ability to fill there?</li>
      <li>Did recruiter proactively communicate with BDM the challenges of the requirement?</li>
    </ul></div>

    <div class="activity red">Interview</div>
    <div class="practices plain red"><ul class="checks">
      <li>Did they finish 1 through 10?</li>
      <li>Do they stop at the first candidate they found rather than finish the search?</li>
      <li>Did they and the BDM ID the perfect candidate correctly?</li>
      <li>Did the customer change the skill set or qualifications they were looking for?</li>
      <li>How many candidates did the customer have in play for this requirement?</li>
    </ul></div>

    <div class="activity blue">Fills</div>
    <div class="practices shade blue"><ul class="checks">
      <li>Did the recruiter dictate what references we needed to verify candidate?</li>
      <li>Confirm reference was don't correctly?</li>
      <li>Did recruiter lead candidate in initial AI?</li>
      <li>Did recruiter lead the references?</li>
      <li>Did recruiter REVIEW Interview Tip Guideline with candidate?</li>
      <li>Did recruiter fill out lock down cells in SubmitLog?</li>
    </ul></div>
  </section>

  <section class="sheet two">
    <div class="activity-head">Recruiting<br>Activity</div>
    <div class="practice-head">Best Practices Verification</div>

    <div class="activity">CN Entered</div>
    <div class="practices"><ul class="checks">
      <li>Are they participating in your proactive recruiting schedule?</li>
      <li>What avenues do they use to source candidates? 1-10</li>
      <li>How well do they know how to parse?</li>
      <li>Are they matching every candidate that they call for an opportunity?</li>
    </ul></div>

    <div class="activity">Contacts</div>
    <div class="practices"><ul class="checks">
      <li>Confirm recruiter has Apex Recruit synced with MailDesk?</li>
      <li>Are they documenting each call they have with candidate?</li>
      <li>Confirm they are parsing ProLink messages into SubmitLog.</li>
      <li>Confirm they are following our screening process.</li>
    </ul></div>

    <div class="activity">Matches</div>
    <div class="practices"><ul class="checks">
      <li>Confirm they are able to ID the perfect candidate.</li>
      <li>Confirm they are going 1 through 10.</li>
      <li>Confirm they can efficiently go 1 through 10.</li>
      <li>Are they going narrow in their initial 1 through 10 search?</li>
      <li>Are they finishing 1 through 10 regardless if they find a candidate early in process?</li>
      <li>Identify what they determine in a candidate's credentials to match.</li>
      <li>Do they have a grasp on all open positions?</li>
      <li>Are there appropriate number of matches for each avenue?</li>
      <li>Have they posted the job? ProLink feed / NetBridge / Beacon Reach</li>
    </ul></div>

    <div class="activity">AIs</div>
    <div class="practices"><ul class="checks">
      <li>Do they proactively recruit on Mondays?</li>
      <li>Confirm they call, email, and ProLink connect with every match.</li>
      <li>Confirm that they continue to call and email every match they had the previous days before sourcing again.</li>
      <li>Confirm recruiter is "warming" voicemails through our past history with candidate or common ground with candidate.</li>
    </ul></div>

    <div class="activity">Submittals</div>
    <div class="practices"><ul class="checks">
      <li>Confirm matches are accurate toward job they are currently working.</li>
      <li>Are they working on the right requirement?</li>
      <li>Is the requirement's moderate ability to fill there?</li>
      <li>Did recruiter proactively communicate with BDM the challenges of the requirement?</li>
    </ul></div>

    <div class="activity">Interview</div>
    <div class="practices"><ul class="checks">
      <li>Did they finish 1 through 10?</li>
      <li>Do they stop at the first candidate they found rather than finish the search?</li>
      <li>Did they and the BDM ID the perfect candidate correctly?</li>
      <li>Did the customer change the skill set or qualifications they were looking for?</li>
      <li>How many candidates did the customer have in play for this requirement?</li>
    </ul></div>

    <div class="activity">Fills</div>
    <div class="practices"><ul class="checks">
      <li>Did the recruiter dictate what references we needed to verify candidate?</li>
      <li>Confirm reference was don't correctly?</li>
      <li>Did recruiter lead candidate in initial AI?</li>
      <li>Did recruiter lead the references?</li>
      <li>Did recruiter REVIEW Interview Tip Guideline with candidate?</li>
      <li>Did recruiter fill out lock down cells in SubmitLog?</li>
    </ul></div>
  </section>
</div>
</body>
</html>
```